We need a designer to help us represent our unique approach to creating lesson plans for digital learning. At the Seasonal Academy for Screen Fluency, held in Providence RI this July 13 - 18, we'll use your design with 100 teachers and then put it online to reach hundreds of thousands more.

We have a draft visual of our model that we like - but it's not pretty (Since we are not designers, it looks a little clunky).

Please create a simple and attractive design in two versions: (1) one that we can use as a 1-page printed handout and (2) one that we can use where teachers can fill in sections and write ideas under each section of the graphic.

Why you should bid on this job? We're a leading provider of digital and media literacy curriculum resources with a huge international and national audience. Working with us will establish your expertise in the area of educational multimedia design.

Target Market(s)

Elementary and secondary teachers in public schools

Industry/Entity Type

Digital

Font styles to use
Sans Serif

Requirements
Must have
• TITLE : Digital Literacy Curriculum Framework

1 page version - suitable for use as a poster or 1-page flyer

Fillable form version - suitable for use as a handout with spaces for teachers to write

```html
<!DOCTYPE html>
<html lang="en">
<head>
<meta charset="utf-8">
<title>Digital Literacy Curriculum Framework</title>
<link rel="stylesheet" href="https://fonts.googleapis.com/css2?family=Open+Sans:wght@400;600;700&display=swap">
<style>
  :root {
    --page: #ffffff;
    --sheet: #fdf3e9;
    --sheet-edge: #e4ddd5;
    --navy: #155799;
    --title: #1a5494;
    --sky: #4a9fea;
    --sand: #fed396;
    --task-text: #1f5593;
    --orange: #fe6629;
    --white: #ffffff;
  }
  html, body {
    margin: 0;
    padding: 0;
    width: 950px;
    height: 1200px;
    overflow: hidden;
    background: var(--page);
  }
  .framework {
    display: block;
    width: 950px;
    height: 1200px;
    font-family: "Open Sans", sans-serif;
  }
  .sheet { fill: var(--sheet); stroke: var(--sheet-edge); stroke-width: 1; }
  .title { fill: var(--title); font-size: 32px; font-weight: 700; }
  .pillar-box { fill: var(--navy); }
  .pillar-label { fill: var(--white); font-size: 27px; font-weight: 400; }
  .element-circle { fill: var(--orange); }
  .element-label { fill: var(--white); font-size: 17px; font-weight: 600; }
  .ring { fill: var(--sky); }
  .ring-label { fill: var(--white); font-size: 13px; font-weight: 600; letter-spacing: 0.5px; }
  .task-box { fill: var(--sand); }
  .task-label { fill: var(--task-text); font-size: 18px; font-weight: 600; }
</style>
</head>
<body>
<svg class="framework" viewBox="0 0 792 1000" preserveAspectRatio="xMidYMid meet" role="img" aria-label="Digital Literacy Curriculum Framework diagram">
  <g transform="translate(-4 0)">
    <rect class="sheet" x="42" y="42" width="708" height="916"/>

    <text class="title" x="396" y="99" text-anchor="middle">Digital Literacy Curriculum Framework</text>

    <!-- Four pillars -->
    <g class="pillar">
      <rect class="pillar-box" x="81" y="211" width="169" height="56" rx="5"/>
      <text class="pillar-label" x="165.5" y="249" text-anchor="middle">Purpose</text>
    </g>
    <g class="pillar">
      <rect class="pillar-box" x="535" y="211" width="169" height="56" rx="5"/>
      <text class="pillar-label" x="619.5" y="249" text-anchor="middle">Assessment</text>
    </g>
    <g class="pillar">
      <rect class="pillar-box" x="81" y="733" width="169" height="56" rx="5"/>
      <text class="pillar-label" x="165.5" y="771" text-anchor="middle">Content</text>
    </g>
    <g class="pillar">
      <rect class="pillar-box" x="541" y="733" width="169" height="56" rx="5"/>
      <text class="pillar-label" x="625.5" y="771" text-anchor="middle">Pedagogy</text>
    </g>

    <!-- Elements -->
    <g class="element">
      <circle class="element-circle" cx="293" cy="352" r="63"/>
      <text class="element-label" x="293" y="358" text-anchor="middle">Standards</text>
    </g>
    <g class="element">
      <circle class="element-circle" cx="500" cy="353" r="63"/>
      <text class="element-label" x="497" y="348" text-anchor="middle">Work</text>
      <text class="element-label" x="500" y="369" text-anchor="middle">Products</text>
    </g>
    <g class="element">
      <circle class="element-circle" cx="229" cy="546" r="63"/>
      <text class="element-label" x="229" y="552" text-anchor="middle">Texts</text>
    </g>
    <g class="element">
      <circle class="element-circle" cx="562" cy="552" r="63"/>
      <text class="element-label" x="562" y="547" text-anchor="middle">Instructional</text>
      <text class="element-label" x="562" y="568" text-anchor="middle">Strategies</text>
    </g>
    <g class="element">
      <circle class="element-circle" cx="395" cy="670" r="63"/>
      <text class="element-label" x="395" y="676" text-anchor="middle">Tools</text>
    </g>

    <!-- Core: task within its contexts -->
    <g class="core">
      <circle class="ring" cx="396" cy="495" r="112"/>
      <text class="ring-label" x="396" y="410" text-anchor="middle">Learners</text>
      <text class="ring-label" x="396" y="589" text-anchor="middle">Context</text>
      <text class="ring-label" transform="translate(310 495) rotate(-90)" text-anchor="middle">Self</text>
      <text class="ring-label" transform="translate(478 495) rotate(90)" text-anchor="middle">Community</text>
      <rect class="task-box" x="323" y="421" width="146" height="148" rx="6"/>
      <text class="task-label" x="396" y="487" text-anchor="middle">TASK or</text>
      <text class="task-label" x="396" y="508" text-anchor="middle">ACTIVITY</text>
    </g>
  </g>
</svg>
</body>
</html>
```